Business Card for Brevel Coatings

We need a simple, yet out standing business card for our painting company.

Target Market(s)

wealthy; high-end neighborhoods, and businesses

Industry/Entity Type

Painting

Contact Information for Business Card

Name:
Doran Vask

Email:
d.vask@brevel-coatings.com

Website:
Brevel-coatings.com

Phone Number:
(555) 416-9073

Font styles to use
Serif
Sans Serif

Requirements
Must have
• slogan "Refined Color Finishes"
Should not have
• A title attached to the name on the card

```html
<!DOCTYPE html>
<html lang="en">
<head>
<meta charset="utf-8">
<title>Brevel Coatings — Business Card</title>
<link rel="stylesheet" href="https://fonts.googleapis.com/css2?family=Cinzel:wght@400;600;700&family=Crimson+Text:wght@400;600&display=swap">
<style>
  :root {
    --backdrop: #2e3d45;
    --forest: #46592a;
    --forest-deep: #34481c;
    --forest-emboss: #566b33;
    --lime: #a9c63a;
    --paper: #ffffff;
    --ink: #2b3a17;
    --rule: #3b4a24;
  }
  * { box-sizing: border-box; margin: 0; padding: 0; }
  html, body { width: 1200px; height: 900px; overflow: hidden; }
  body {
    background: var(--backdrop);
    font-family: "Crimson Text", Georgia, serif;
    position: relative;
  }
  .card {
    position: absolute;
    left: 280px;
    width: 640px;
    height: 366px;
    overflow: hidden;
  }

  /* Shared wordmark */
  .wordmark {
    display: flex;
    align-items: center;
    gap: 14px;
  }
  .wordmark-name {
    font-family: "Cinzel", serif;
    font-weight: 600;
    display: flex;
    flex-direction: column;
    line-height: 1;
  }
  .wordmark-name .line-main { letter-spacing: 1px; }
  .wordmark-name .line-sub { letter-spacing: 7px; margin-top: 4px; }
  .mark-dot { border-radius: 50%; flex: none; }

  /* Back side */
  .card-back {
    top: 60px;
    background: var(--forest);
    display: flex;
    flex-direction: column;
    align-items: center;
    justify-content: center;
  }
  .card-back .wordmark { color: var(--forest-emboss); }
  .card-back .mark-dot {
    width: 56px; height: 56px;
    background: var(--forest-emboss);
  }
  .card-back .line-main { font-size: 46px; }
  .card-back .line-sub { font-size: 24px; letter-spacing: 9px; }
  .card-back .slogan {
    font-family: "Cinzel", serif;
    font-size: 15px;
    letter-spacing: 5px;
    color: var(--forest-emboss);
    margin-top: 14px;
  }

  /* Front side */
  .card-front {
    top: 474px;
    background: var(--paper);
  }
  .front-body {
    position: absolute;
    top: 0; left: 0; right: 0;
    height: 312px;
    display: flex;
    align-items: center;
    padding-left: 40px;
  }
  .card-front .wordmark { color: var(--ink); }
  .card-front .mark-dot {
    width: 44px; height: 44px;
    background: var(--lime);
  }
  .card-front .line-main { font-size: 36px; }
  .card-front .line-sub { font-size: 19px; letter-spacing: 6.5px; }
  .divider {
    width: 1px;
    height: 126px;
    background: var(--rule);
    margin: 0 16px 0 24px;
  }
  .contact .person {
    font-family: "Cinzel", serif;
    font-weight: 700;
    font-size: 21px;
    color: var(--ink);
    margin-bottom: 10px;
  }
  .contact ul { list-style: none; }
  .contact li {
    display: flex;
    align-items: center;
    gap: 10px;
    font-size: 15px;
    color: var(--ink);
    height: 28px;
    white-space: nowrap;
  }
  .contact svg { width: 18px; height: 18px; flex: none; }
  .stripe-lime {
    position: absolute; left: 0; right: 0; top: 312px; height: 6px;
    background: var(--lime);
  }
  .band-forest {
    position: absolute; left: 0; right: 0; top: 322px; bottom: 0;
    background: var(--forest-deep);
  }
</style>
</head>
<body>
  <section class="card card-back" aria-label="Card back">
    <div class="wordmark">
      <span class="mark-dot"></span>
      <span class="wordmark-name"><span class="line-main">Brevel</span><span class="line-sub">Coatings</span></span>
    </div>
    <p class="slogan">Refined Color Finishes</p>
  </section>

  <section class="card card-front" aria-label="Card front">
    <div class="front-body">
      <div class="wordmark">
        <span class="mark-dot"></span>
        <span class="wordmark-name"><span class="line-main">Brevel</span><span class="line-sub">Coatings</span></span>
      </div>
      <div class="divider"></div>
      <div class="contact">
        <p class="person">Doran Vask</p>
        <ul>
          <li>
            <svg viewBox="0 0 24 24"><path fill="#2b3a17" d="M6.6 10.8c1.4 2.8 3.8 5.1 6.6 6.6l2.2-2.2c.3-.3.7-.4 1-.2 1.1.4 2.3.6 3.6.6.6 0 1 .4 1 1V20c0 .6-.4 1-1 1C10.6 21 3 13.4 3 4c0-.6.4-1 1-1h3.5c.6 0 1 .4 1 1 0 1.3.2 2.5.6 3.6.1.3 0 .7-.2 1z"/></svg>
            (555) 416-9073
          </li>
          <li>
            <svg viewBox="0 0 24 24" fill="none" stroke="#2b3a17" stroke-width="1.6"><rect x="3" y="5" width="18" height="14"/><path d="M3 5l9 8 9-8M3 19l7-7M21 19l-7-7"/></svg>
            d.vask@brevel-coatings.com
          </li>
          <li>
            <svg viewBox="0 0 24 24" fill="none" stroke="#2b3a17" stroke-width="1.4"><circle cx="12" cy="12" r="9"/><ellipse cx="12" cy="12" rx="4" ry="9"/><path d="M3 12h18M4.5 7.5h15M4.5 16.5h15"/></svg>
            www.brevel-coatings.com
          </li>
        </ul>
      </div>
    </div>
    <div class="stripe-lime"></div>
    <div class="band-forest"></div>
  </section>
</body>
</html>
```